Leadership Seminar Concept

We want the theme picture/design of the Leadership Seminar Flyer with theme "Inspiring Commitment"

Industry/Entity Type

Leadership

```html
<!DOCTYPE html>
<html lang="en">
<head>
<meta charset="utf-8">
<title>Inspiring Commitment – Leadership Seminar Flyer</title>
<link href="https://fonts.googleapis.com/css2?family=Oswald:wght@200;400;600;700&family=Open+Sans:wght@400;700&display=swap" rel="stylesheet">
<style>
  :root {
    --backdrop: #cfcfcf;
    --chalkboard: #2b2b2b;
    --chalk-soft: #363636;
    --chalk-line: #e6e6e6;
    --gold: #f2c500;
    --band: #e9b410;
    --ink-white: #ffffff;
    --body-grey: #d8d8d8;
    --plum: #5b1b5e;
    --band-ink: #2a2a2a;
  }
  * { margin: 0; padding: 0; box-sizing: border-box; }
  html, body { width: 1200px; height: 800px; overflow: hidden; background: var(--backdrop); }

  .flyer {
    position: absolute; left: 330px; top: 30px;
    width: 540px; height: 740px;
    background: var(--chalkboard);
    overflow: hidden;
    font-family: "Open Sans", sans-serif;
  }

  .cord { position: absolute; top: 0; width: 2px; background: var(--chalk-line); }
  .cord--idea { left: 243px; height: 112px; }
  .cord--side { left: 414px; height: 70px; }

  .art-bulb { position: absolute; background: var(--chalk-soft); border-radius: 4px; }
  .art-bulb--idea { left: 157px; top: 112px; width: 146px; height: 196px; }
  .art-bulb--side { left: 383px; top: 70px; width: 64px; height: 130px; }

  .title {
    position: absolute; left: 70px; top: 22px; width: 162px;
    text-align: right; font-family: "Oswald", sans-serif; text-transform: uppercase;
    line-height: 0.95; z-index: 2;
  }
  .title__strong { display: block; color: var(--gold); font-weight: 700; font-size: 36px; }
  .title__light { display: block; color: var(--ink-white); font-weight: 200; font-size: 33px; letter-spacing: -0.5px; }

  .portrait {
    position: absolute; left: 140px; top: 335px; width: 186px; height: 333px;
    background: linear-gradient(180deg, #6e5446 0%, #b98a70 35%, #27324a 72%, #1d2436 100%);
  }

  .promise-box {
    position: absolute; left: 322px; top: 208px; width: 170px; height: 200px;
    border: 1.5px solid var(--gold);
    padding: 9px 7px 0 4px;
    text-align: right;
    font-family: "Oswald", sans-serif; text-transform: uppercase;
    font-weight: 400; font-size: 24px; line-height: 1.05; letter-spacing: -0.8px;
    color: var(--ink-white);
  }
  .promise-box em { font-style: normal; font-weight: 600; color: var(--gold); }

  .note { position: absolute; font-size: 9px; line-height: 1.3; color: var(--body-grey); }
  .note strong { color: var(--gold); font-weight: 700; }
  .note--commitment { left: 24px; top: 405px; width: 110px; }
  .note--shiftability { left: 336px; top: 424px; width: 120px; }

  .invite-band {
    position: absolute; left: 0; bottom: 0; width: 540px; height: 72px;
    background: var(--band);
    padding: 14px 40px 0 44px;
    font-size: 13px; line-height: 1.35; color: var(--band-ink);
  }
  .invite-band__initial { color: var(--plum); font-weight: 700; font-size: 22px; line-height: 0; }
</style>
</head>
<body>
  <main class="flyer">
    <span class="cord cord--idea"></span>
    <span class="cord cord--side"></span>
    <div class="art-bulb art-bulb--idea" role="img" aria-label="Chalk drawing of a glowing yellow light bulb with the word idea"></div>
    <div class="art-bulb art-bulb--side" role="img" aria-label="Chalk drawing of a white hanging light bulb"></div>

    <h1 class="title">
      <span class="title__strong">Inspiring</span>
      <span class="title__light">Commitment</span>
    </h1>

    <div class="portrait" role="img" aria-label="Photo of a young businessman in glasses and a suit looking up toward the light bulb"></div>

    <p class="promise-box">
      Shifting <em>Self,</em><br>
      Your <em>People</em><br>
      And your<br>
      <em>Organization</em><br>
      From <em>Static</em> to<br>
      <em>Movement</em> to<br>
      <em>Momentum</em>
    </p>

    <p class="note note--commitment">
      <strong>Inspiring commitment is enabling others to act.</strong>
      It involves energizing individuals to strive towards a compelling vision of the future, guiding people through change, keeping everyone aligned, building trust and open channels of communication, while reinforcing success.
    </p>

    <p class="note note--shiftability">
      <strong>Shiftability is responding to outward demands from inward strength, purpose and skill.</strong>
      The mindset of shiftability acknowledges the need for change and embraces it, keeping an open mind about new ideas while wisely retaining things that still apply – always learning, always building, always growing.
    </p>

    <p class="invite-band">
      <span class="invite-band__initial">W</span>e invite you to a journey of greatness where you'll learn and practice tools for thriving as a leader by inspiring momentum.
    </p>
  </main>
</body>
</html>
```